Selam-Kaveh - Promote and Support a community

Design a website for Ethiopean Community. the design should be friendly, easy to navigate and maintain the look & feel of the Ethiopian culture. a proposed logo is attached but it can be change according to your recommendations. This is a project we are doing at a discount rate as it supports a weak community.
Please visit their current website http://www.selam-kaveh.example.org/index.php?lang=en

Target Market(s)

Community members, potential doners

Industry/Entity Type

community

Number of Pages Required

1 page

Font styles to use
Sans Serif

Requirements
Must have
• easy to navigate friendly interface

```html
<!DOCTYPE html>
<html lang="en">
<head>
<meta charset="utf-8">
<title>Selam-Kaveh – Community Health</title>
<link href="https://fonts.googleapis.com/css2?family=Montserrat:wght@400;500;600;700&display=swap" rel="stylesheet">
<style>
:root{
  --green:#0f6a3b;
  --green-dark:#0b5330;
  --red:#b5121b;
  --red-dark:#8f0c12;
  --ink:#1d1d1d;
  --muted:#444;
  --bg-soft:#f5f5f5;
  --hero:#3b2f1f;
}
*{box-sizing:border-box;margin:0;padding:0}
html,body{width:1200px;height:3840px;overflow:hidden}
body{font-family:"Montserrat",sans-serif;color:var(--ink);background:#fff;position:relative}
.btn{display:inline-flex;align-items:center;justify-content:center;color:#fff;font-size:15px;font-weight:500;background:linear-gradient(#c5161f,var(--red-dark));border-radius:2px;text-decoration:none}
.btn.green{background:linear-gradient(#13804a,var(--green-dark))}

/* header */
.topbar{height:119px;position:relative}
.brand{position:absolute;left:62px;top:16px;display:flex;align-items:center;gap:10px}
.brand .mark{width:28px;height:28px;border-radius:50%;background:var(--red)}
.brand span{font-size:20px;font-weight:700;color:var(--green)}
.reg{position:absolute;left:0;right:0;top:24px;text-align:center;font-size:13px;color:var(--green);line-height:21px}
.reg b{display:block;color:var(--red);font-size:22px;font-weight:700;margin-top:3px}
.top-donate{position:absolute;left:831px;top:39px;width:147px;height:39px}
.lang{position:absolute;left:991px;top:39px;width:147px;height:39px;font-size:14px;gap:6px}
.lang i{width:16px;height:16px;border-radius:50%;background:#fff;display:block}
.nav{height:45px;background:var(--green);display:flex;padding-left:62px}
.nav a{color:#fff;font-size:11.5px;text-decoration:none;display:flex;align-items:center;justify-content:center;width:112px}
.nav a.on{background:var(--red)}

/* hero */
.hero{height:511px;position:relative;background:linear-gradient(180deg,#5a4a30 0%,#3a2d1c 55%,#1e1710 100%)}
.hero h1{position:absolute;top:285px;left:0;right:0;text-align:center;color:#fff;font-size:32px;font-weight:700;line-height:38px}
.hero .btn{position:absolute;left:475px;top:383px;width:249px;height:49px;font-size:18px}
.scroll{position:absolute;left:1096px;top:491px;width:41px;height:41px;border-radius:50%;background:var(--green);display:flex;align-items:center;justify-content:center}

/* welcome */
.welcome{height:465px;background:var(--bg-soft);position:relative}
.frame{position:absolute;background:#fff;padding:8px;box-shadow:0 2px 8px rgba(0,0,0,.18)}
.frame div{width:100%;height:100%}
.welcome .frame{left:124px;top:88px;width:372px;height:283px}
.section-title{font-size:32px;font-weight:700;color:var(--green)}
.welcome h2{position:absolute;left:558px;top:84px}
.welcome p{position:absolute;left:558px;top:152px;width:520px;font-size:14.5px;line-height:24px;color:var(--ink)}
.welcome .btn{position:absolute;left:558px;top:322px;width:212px;height:40px}

/* programs */
.programs{height:946px;position:relative}
.programs h2{position:absolute;left:124px;top:95px}
.rule{display:block;width:120px;height:3px;background:var(--red);margin-top:10px}
.grid{position:absolute;left:124px;top:180px;display:grid;grid-template-columns:repeat(3,300px);column-gap:25px;row-gap:0}
.card{height:311px}
.card .pic{height:200px;position:relative}
.card .num{position:absolute;left:0;top:0;width:45px;height:45px;background:var(--red);color:#fff;font-weight:600;font-size:17px;display:flex;align-items:center;justify-content:center}
.card h3{margin-top:12px;font-size:19px;font-weight:500;color:var(--green);line-height:29px}
.programs .btn{position:absolute;left:475px;top:806px;width:249px;height:49px;font-size:18px}

/* mission */
.mission{height:626px;background:var(--bg-soft);position:relative}
.mission .frame{left:126px;top:95px;width:372px;height:435px}
.mission h2{position:absolute;left:592px;top:160px}
.mission p{position:absolute;left:592px;top:242px;width:490px;font-size:14.5px;line-height:24px}
.mission .btn{position:absolute;top:415px;width:212px;height:42px}

/* partners */
.partners{height:335px;position:relative;text-align:center}
.partners h2{padding-top:90px}
.partners .rule{margin:12px auto 0}
.logos{position:absolute;left:124px;right:124px;top:180px;display:flex;justify-content:space-between;align-items:center}
.logos span{display:block;background:#bfbfbf;border-radius:4px}

/* contact */
.contact{height:660px;position:relative;background:linear-gradient(180deg,#5e4a1c 0%,#3a2c14 40%,#1a140c 100%)}
.contact h2{position:absolute;top:85px;left:0;right:0;text-align:center;color:#fff;font-size:32px;font-weight:700}
.contact .lead{position:absolute;top:153px;left:0;right:0;text-align:center;color:#fff;font-size:14px;line-height:22px}
.info{position:absolute;left:180px;display:flex;gap:18px;color:#fff}
.info .ic{width:46px;height:46px;border-radius:50%;background:var(--red);display:flex;align-items:center;justify-content:center;flex:none;margin-top:8px}
.info h4{color:#23a35c;font-size:20px;font-weight:600}
.info p{font-size:14px;font-style:italic;line-height:22px}
.field{position:absolute;background:#fff;font-size:12px;color:#333;padding:18px 19px 0}
.send{position:absolute;left:887px;top:520px;width:129px;height:44px;gap:12px}

/* footer */
.footer{height:133px;background:#171311;position:relative}
.footer .up{position:absolute;left:1096px;top:-24px;width:41px;height:41px;border-radius:50%;background:var(--green);display:flex;align-items:center;justify-content:center}
.fnav{display:flex;justify-content:space-between;padding:34px 55px 0 62px}
.fnav a{color:#fff;font-size:14px;text-decoration:none}
.fnav a.on{color:#22a35c}
.copy{position:absolute;left:62px;bottom:10px;font-size:9px;color:#888}
.social{position:absolute;right:62px;bottom:10px;display:flex;gap:6px}
.social i{display:block;width:9px;height:9px;background:#888}
</style>
</head>
<body>

<header class="topbar">
  <div class="brand"><i class="mark"></i><span>Selam-Kaveh</span></div>
  <div class="reg">Selam Health - Community Health Promotion<br>Association Registered Number:<b>581239047</b></div>
  <a class="btn top-donate" href="#">Donate Now</a>
  <a class="btn green lang" href="#"><i></i>English
    <svg width="9" height="6" viewBox="0 0 9 6"><path d="M1 1l3.5 3.5L8 1" stroke="#fff" fill="none" stroke-width="1.3"/></svg></a>
</header>

<nav class="nav">
  <a class="on" href="#">Home</a><a href="#">About Us ⌄</a><a href="#">The Community</a><a href="#">Programs ⌄</a><a href="#">Video Gallery</a><a href="#">News ⌄</a><a href="#">Advocacy</a><a href="#">Partners</a><a href="#">Support Us</a>
</nav>

<section class="hero" role="img" aria-label="Crowd of women from the community in traditional white shawls">
  <h1>Selam-Kaveh is dedicated to improving the<br>health of the Ethiopian Israeli Community</h1>
  <a class="btn" href="#">Learn More</a>
  <div class="scroll"><svg width="16" height="10" viewBox="0 0 16 10"><path d="M2 2l6 6 6-6" stroke="#fff" fill="none" stroke-width="2"/></svg></div>
</section>

<section class="welcome">
  <div class="frame"><div role="img" aria-label="Children and women gathered closely together" style="background:linear-gradient(135deg,#3b2a22,#7a5140 50%,#2f5a35)"></div></div>
  <h2 class="section-title">Welcome to Selam-Kaveh</h2>
  <p>Selam-Kaveh was founded in 1999 by Dr. Miriam Levanon, Head of the Endocrinology Unit at the Carmel Valley Medical Center. Her experience with Ethiopian patients made her realize that medical treatment could not succeed without culturally competent communication. Working with a team of Ethiopian-Israeli healthcare professionals who were closely familiar with Ethiopian social and cultural history, . . .</p>
  <a class="btn" href="#">Read More</a>
</section>

<section class="programs">
  <h2 class="section-title">Our Programs<span class="rule"></span></h2>
  <div class="grid">
    <div class="card"><div class="pic" role="img" aria-label="Presenter speaking to a seated audience" style="background:linear-gradient(135deg,#7d8aa0,#3e4658)"><span class="num">1</span></div><h3>Health &amp; Education<br>Presentations</h3></div>
    <div class="card"><div class="pic" role="img" aria-label="Community members at a health fair table" style="background:linear-gradient(135deg,#c9c2b4,#6b6256)"><span class="num">2</span></div><h3>Regional Health Fairs</h3></div>
    <div class="card"><div class="pic" role="img" aria-label="Presenters in a radio studio" style="background:linear-gradient(135deg,#b7b8b6,#4d4a48)"><span class="num">3</span></div><h3>Amharic Radio Program</h3></div>
    <div class="card"><div class="pic" role="img" aria-label="Group exercise session with raised arms" style="background:linear-gradient(135deg,#b9c7cf,#5a6b76)"><span class="num">4</span></div><h3>Health Leadership<br>Development</h3></div>
    <div class="card"><div class="pic" role="img" aria-label="Women at a cookery course table" style="background:linear-gradient(135deg,#3f7c69,#d8a24a)"><span class="num">5</span></div><h3>Nutrition &amp; Cookery Courses</h3></div>
    <div class="card"><div class="pic" role="img" aria-label="Group of healthcare staff in a training room" style="background:linear-gradient(135deg,#d9c9a6,#7a5a3e)"><span class="num">6</span></div><h3>Healthcare Personnel Training</h3></div>
  </div>
  <a class="btn" href="#">See More</a>
</section>

<section class="mission">
  <div class="frame"><div role="img" aria-label="Smiling children outdoors" style="background:linear-gradient(160deg,#c44a42,#6b4a38 40%,#9fc4dc)"></div></div>
  <h2 class="section-title">Our Missions &amp; Goals<span class="rule"></span></h2>
  <p>Selam-Kaveh (“health” in both Amharic and Hebrew) is dedicated to improving the health of the Ethiopian Israeli community, and firmly believes in the right of every Israeli citizen to access proper health care. Selam-Kaveh believes that fostering an informed, active health leadership from within the community itself is key to achieving its goals.</p>
  <a class="btn" href="#" style="left:595px">Donate Now</a>
  <a class="btn green" href="#" style="left:834px">Contact Us</a>
</section>

<section class="partners">
  <h2 class="section-title">Our Partners</h2><span class="rule"></span>
  <div class="logos">
    <span style="width:55px;height:62px"></span>
    <span style="width:125px;height:60px"></span>
    <span style="width:145px;height:36px"></span>
    <span style="width:90px;height:62px"></span>
    <span style="width:175px;height:36px"></span>
    <span style="width:70px;height:62px"></span>
  </div>
</section>

<section class="contact" role="img" aria-label="Portrait of a woman in a yellow headscarf">
  <h2>Contact Us</h2>
  <p class="lead">Lorem ipsum dolor sit amet, consectetur adipiscing elit, sed do eiusmod<br>tempor incididunt ut labore et dolore magna aliqua.</p>
  <div class="info" style="top:245px"><span class="ic"><svg width="20" height="22" viewBox="0 0 20 22"><path d="M10 21s-7-7-7-12a7 7 0 0114 0c0 5-7 12-7 12z" stroke="#fff" fill="none" stroke-width="1.8"/><circle cx="10" cy="9" r="2.5" stroke="#fff" fill="none" stroke-width="1.8"/></svg></span><div><h4>Office</h4><p>Harbor 12/4 POB 2140<br>Netanya, 42150</p></div></div>
  <div class="info" style="top:357px"><span class="ic"><svg width="22" height="16" viewBox="0 0 22 16"><rect x="1" y="1" width="20" height="14" stroke="#fff" fill="none" stroke-width="1.6"/><path d="M1 1l10 8 10-8" stroke="#fff" fill="none" stroke-width="1.6"/></svg></span><div><h4>Email</h4><p>selamkaveh@example.org</p></div></div>
  <div class="info" style="top:458px"><span class="ic"><svg width="20" height="20" viewBox="0 0 20 20"><path d="M5 2l3 4-2 2c1 2 3 4 5 5l2-2 4 3-2 3C9 17 3 11 2 5z" stroke="#fff" fill="none" stroke-width="1.6"/></svg></span><div><h4>Phone</h4><p>04-5550192</p></div></div>
  <div class="field" style="left:476px;top:248px;width:260px;height:42px">First Name*</div>
  <div class="field" style="left:756px;top:248px;width:260px;height:42px">Last Name*</div>
  <div class="field" style="left:476px;top:313px;width:260px;height:42px">Email Address*</div>
  <div class="field" style="left:756px;top:313px;width:260px;height:42px">Phone Number</div>
  <div class="field" style="left:476px;top:378px;width:540px;height:118px">Describe your Request*</div>
  <a class="btn send" href="#">Send <svg width="20" height="18" viewBox="0 0 20 18"><path d="M1 8L19 1 15 17 10 11z" fill="#fff"/></svg></a>
</section>

<footer class="footer">
  <div class="up"><svg width="16" height="10" viewBox="0 0 16 10"><path d="M2 8l6-6 6 6" stroke="#fff" fill="none" stroke-width="2"/></svg></div>
  <div class="fnav"><a class="on" href="#">Home</a><a href="#">About Us</a><a href="#">The Community</a><a href="#">Programs</a><a href="#">Video Gallery</a><a href="#">News</a><a href="#">Advocacy</a><a href="#">Partners</a><a href="#">Support Us</a></div>
  <div class="copy">Copyright © 2022 Selam-Kaveh &nbsp;|&nbsp; Privacy Policy &nbsp;|&nbsp; Terms &amp; Conditions</div>
  <div class="social"><i></i><i></i></div>
</footer>

</body>
</html>
```